strength and conditioning business focused on helping people move more efficiently

I need a business card designed for a Philadelphia based company called Brk Stn Motion (pronounced Brick Stone). We offer fitness professional services with the idea of helping people feel better and move optimally. We do this by designing and walking through individualized programs as well as minor soft tissue work. Our perfect client would be athletes but we will be marketing to parents who have children that are active They remember their former athletic days and want to get as close as possible back to that feeling. Attached will be the official logo and logo formats. I would love for the design to communicate trustworthy and creative. I would also love for the design to be square with rounded edges.

Target Market(s)

Parents of athletic children
former athletes
athletes

Industry/Entity Type

Fitness

Contact Information for Business Card

Business: Brk Stn Athletics
Name: Coach Gareth Milford
Position: Strength and Conditioning Coach / Certified Personal Trainer
Contact: coach.mil@brkstn.example
Text: (555)204-7719

Font styles to use
Serif
Sans Serif

Colors
fbee38
fbee3e
0255a3
3176b5
ffffff

Requirements
Must have
• use of logo
Nice to have
• Square design
rounded edges

```html
<!DOCTYPE html>
<html lang="en">
<head>
<meta charset="utf-8">
<title>Brk Stn Motion – Business Card</title>
<link rel="stylesheet" href="https://fonts.googleapis.com/css2?family=Open+Sans:wght@400;600;700;800&display=swap">
<style>
  :root {
    --page: #e9e9e9;
    --card-blue: #034a8c;
    --accent-yellow: #f6c417;
    --text-white: #ffffff;
  }
  * { margin: 0; padding: 0; box-sizing: border-box; }
  html, body { width: 1200px; height: 960px; overflow: hidden; }
  body {
    background: var(--page);
    font-family: "Open Sans", Arial, sans-serif;
    position: relative;
  }
  .card {
    position: absolute;
    top: 277px;
    width: 402px;
    height: 402px;
    border-radius: 38px;
    background: var(--card-blue);
    color: var(--text-white);
  }
  .card--front { left: 170px; }
  .card--back { left: 623px; }

  .brand {
    position: absolute;
    inset: 0;
    display: flex;
    flex-direction: column;
    align-items: center;
    justify-content: center;
  }
  .brand__dot {
    width: 72px;
    height: 72px;
    border-radius: 50%;
    background: var(--accent-yellow);
    margin-bottom: 18px;
  }
  .brand__name {
    font-weight: 800;
    font-size: 66px;
    line-height: 0.98;
    text-align: center;
    color: var(--text-white);
    letter-spacing: -1px;
  }

  .person {
    position: absolute;
    right: 27px;
    top: 137px;
    text-align: right;
  }
  .person__name {
    font-weight: 700;
    font-size: 17px;
    color: var(--accent-yellow);
    line-height: 24px;
  }
  .person__role {
    font-size: 13px;
    line-height: 19px;
  }
  .business {
    position: absolute;
    left: 28px;
    top: 274px;
  }
  .business__name {
    font-weight: 700;
    font-size: 15px;
    margin-bottom: 9px;
  }
  .contact-list { list-style: none; }
  .contact-list li {
    display: flex;
    align-items: center;
    gap: 4px;
    font-size: 13px;
    line-height: 19px;
  }
  .contact-list svg { width: 14px; height: 14px; flex: none; }
</style>
</head>
<body>
  <section class="card card--front">
    <div class="brand">
      <div class="brand__dot"></div>
      <div class="brand__name">Brk Stn<br>Motion</div>
    </div>
  </section>

  <section class="card card--back">
    <div class="person">
      <p class="person__name">Coach Gareth Milford</p>
      <p class="person__role">Strength and Conditioning Coach</p>
      <p class="person__role">Certified Personal Trainer</p>
    </div>
    <div class="business">
      <p class="business__name">Brk Stn Athletics</p>
      <ul class="contact-list">
        <li>
          <svg viewBox="0 0 14 14"><circle cx="7" cy="7" r="7" fill="#f6c417"/><path d="M4.3 3.5l1.5-.3.8 1.9-.9.7c.5 1 1.3 1.8 2.3 2.3l.7-.9 1.9.8-.3 1.5c-3.4.3-6.3-2.6-6-6z" fill="#034a8c"/></svg>
          (555) 204-7719
        </li>
        <li>
          <svg viewBox="0 0 14 14"><circle cx="7" cy="7" r="7" fill="#f6c417"/><rect x="3.5" y="4.5" width="7" height="5" fill="none" stroke="#034a8c" stroke-width="1"/><path d="M3.5 4.5L7 7.5l3.5-3" fill="none" stroke="#034a8c" stroke-width="1"/></svg>
          coach.mil@brkstn.example
        </li>
        <li>
          <svg viewBox="0 0 14 14"><circle cx="7" cy="7" r="7" fill="#f6c417"/><circle cx="7" cy="7" r="3.6" fill="none" stroke="#034a8c" stroke-width="1"/><path d="M3.4 7h7.2M7 3.4c-1.6 2-1.6 5.2 0 7.2M7 3.4c1.6 2 1.6 5.2 0 7.2" fill="none" stroke="#034a8c" stroke-width="0.8"/></svg>
          www.brkstn.example
        </li>
      </ul>
    </div>
  </section>
</body>
</html>
```